Truck Drivers Using App w/Jobsite Checklist

Looking for an 8" x 11" flyer that conveys to our customers (roofing contractors) that our drivers have tablets in each truck that have an app with a jobsite checklist that gives contractors less real time notifications and mistakes are caught with photos.
Should read something like this:
Ever wonder if your material has been delivered? We've got a solution for that!
All Trucks are equipped with dash-mounted tablet.
Here's what you get access to:
- Real Time Email Confirmation of Delivery
- Photos of Material Placement
- Before/After Photo of Driveway
- Material List of Products Delivered
- Homeowner Sign Off
Maybe a collage of the different photos available.
Target Market(s)
Roofing/Building Contractors
Industry/Entity Type
Roofing
Requirements
Must have
- website: www.harborfinchbuild.com
- tagline: Building Relationships, Building Trust - a Tradition Since 1905
- Photoshop format for further editing
Nice to have
- A smooth look to it.
- A collage of the photos avail on app

```html
<!DOCTYPE html>
<html lang="en">
<head>
<meta charset="utf-8">
<title>Harbor Finch Build – Delivery Checklist Flyer</title>
<link rel="stylesheet" href="https://fonts.googleapis.com/css2?family=Jost:wght@400;500;600;700&family=Roboto+Condensed:wght@400;500&display=swap">
<style>
  :root{
    --sky-top:#9fc6e8;
    --sky-bottom:#cde2f4;
    --brand-blue:#1a5ba6;
    --deep-blue:#164e93;
    --navy-text:#1b2747;
    --white:#ffffff;
  }
  *{margin:0;padding:0;box-sizing:border-box}
  html,body{width:850px;height:1200px;overflow:hidden}
  body{background:#ffffff;font-family:"Jost",sans-serif}
  .flyer{position:relative;width:850px;height:1200px;overflow:hidden;
    background:linear-gradient(160deg,var(--sky-top) 0%,#b6d5ef 55%,var(--sky-bottom) 100%)}
  .collage{position:absolute;left:0;top:0;width:850px;height:1200px}

  .brand{position:absolute;left:42px;top:96px;display:flex;align-items:center;gap:14px}
  .brand-dot{width:46px;height:46px;border-radius:50%;background:var(--brand-blue)}
  .brand-name{font-weight:700;font-size:30px;line-height:1.05;color:var(--brand-blue);letter-spacing:.5px}

  .headline{position:absolute;left:50px;top:320px;color:var(--brand-blue);font-weight:700;font-size:49px;line-height:55px;letter-spacing:.3px}
  .tagline{position:absolute;left:51px;top:484px;color:var(--navy-text);font-weight:400;font-size:29px;letter-spacing:.6px}

  .access-band{position:absolute;left:0;top:563px;width:460px;height:46px;background:var(--brand-blue);
    clip-path:polygon(0 0,100% 0,94% 100%,0 100%);color:var(--white);font-weight:600;font-size:23px;line-height:46px;padding-left:48px}

  .benefits{position:absolute;left:48px;top:626px;list-style:none}
  .benefits li{display:flex;align-items:center;gap:13px;height:41px;font-family:"Roboto Condensed",sans-serif;font-size:24px;color:var(--navy-text)}
  .benefits svg{width:15px;height:15px;flex:none}

  .worker-photo{position:absolute;left:0;top:853px;width:240px;height:347px;
    background:linear-gradient(180deg,#b8c6d6 0%,#c9a98a 22%,#d8df52 55%,#7d93b0 100%);border-radius:0 100px 0 0}

  .speech{position:absolute;left:262px;top:894px;width:256px;height:118px;background:var(--deep-blue);border-radius:16px;
    color:var(--white);font-size:17px;line-height:23px;padding:22px 16px}
  .speech::before{content:"";position:absolute;left:-58px;top:64px;border-style:solid;border-width:0 60px 24px 0;border-color:transparent var(--deep-blue) transparent transparent}

  .call-label{position:absolute;left:250px;top:1040px;font-size:30px;color:var(--navy-text)}
  .call-number{position:absolute;left:258px;top:1082px;display:flex;align-items:center;gap:8px;font-weight:700;font-size:31px;color:var(--navy-text)}
  .call-number svg{width:28px;height:28px}

  .web-band{position:absolute;left:212px;top:1138px;width:460px;height:62px;background:var(--brand-blue);
    clip-path:polygon(0 0,100% 0,92% 100%,0 100%);display:flex;align-items:center;padding-left:150px;gap:10px;color:var(--white);font-weight:600;font-size:19px}
  .web-band svg{width:18px;height:18px}
</style>
</head>
<body>
<main class="flyer">
  <svg class="collage" viewBox="0 0 642 885" preserveAspectRatio="none">
    <defs>
      <linearGradient id="cab" x1="0" y1="0" x2="0" y2="1">
        <stop offset="0" stop-color="#e4ecf2"/><stop offset=".45" stop-color="#aab3b8"/><stop offset="1" stop-color="#3c434a"/>
      </linearGradient>
      <linearGradient id="load" x1="0" y1="0" x2="1" y2="1">
        <stop offset="0" stop-color="#7fb3e0"/><stop offset=".45" stop-color="#eef1f4"/><stop offset=".7" stop-color="#d88a8a"/><stop offset="1" stop-color="#3a3f44"/>
      </linearGradient>
      <linearGradient id="truck" x1="0" y1="0" x2="1" y2="1">
        <stop offset="0" stop-color="#7db7e8"/><stop offset=".5" stop-color="#eef2f5"/><stop offset="1" stop-color="#4a5057"/>
      </linearGradient>
      <linearGradient id="stack" x1="0" y1="0" x2="0" y2="1">
        <stop offset="0" stop-color="#5f7a52"/><stop offset=".45" stop-color="#8e9e86"/><stop offset=".7" stop-color="#d9cdb4"/><stop offset="1" stop-color="#8e8a80"/>
      </linearGradient>
      <linearGradient id="drive" x1="0" y1="0" x2="1" y2="1">
        <stop offset="0" stop-color="#5d6670"/><stop offset=".4" stop-color="#9a9c9c"/><stop offset="1" stop-color="#b4b4b0"/>
      </linearGradient>
    </defs>
    <g fill="none" stroke="#ffffff" stroke-width="1.5" opacity=".9">
      <polygon points="282,200 440,42 618,215 455,378"/>
      <polygon points="342,555 465,427 620,575 505,723"/>
      <polygon points="402,840 540,692 650,690 650,890"/>
    </g>
    <polygon points="432,0 642,0 642,215 530,110" fill="url(#cab)" stroke="#fff" stroke-width="4" role="img" aria-label="Photo: all trucks are equipped with a dash-mounted tablet showing the jobsite checklist"/>
    <polygon points="290,200 440,50 610,215 455,370" fill="url(#load)" stroke="#fff" stroke-width="4" role="img" aria-label="Photo of strapped roofing material bundles on a delivery truck"/>
    <polygon points="580,280 642,218 642,345" fill="#1a5ba6"/>
    <polygon points="462,430 550,340 642,420 642,540 555,545" fill="url(#truck)" stroke="#fff" stroke-width="4" role="img" aria-label="Photo of a delivery truck with a boom loader"/>
    <polygon points="350,555 465,435 612,575 505,715" fill="url(#stack)" stroke="#fff" stroke-width="4" role="img" aria-label="Photo of shingle bundles placed on a driveway under a tree"/>
    <polygon points="575,690 642,615 642,740" fill="#1a5ba6"/>
    <polygon points="410,840 540,700 642,690 642,885 470,885" fill="url(#drive)" stroke="#fff" stroke-width="4" role="img" aria-label="Photo of a clean concrete driveway after delivery"/>
  </svg>

  <div class="brand">
    <span class="brand-dot"></span>
    <span class="brand-name">HARBOR FINCH<br>BUILD</span>
  </div>

  <h1 class="headline">BUILDING<br>RELATIONSHIPS<br>BUILDING TRUST</h1>
  <p class="tagline">A TRADITION SINCE 1905</p>

  <div class="access-band">Here's what you get access to:</div>
  <ul class="benefits">
    <li><svg viewBox="0 0 16 16"><path d="M2 2 L14 8 L2 14 L5 8 Z" fill="none" stroke="#1a5ba6" stroke-width="1.6" stroke-linejoin="round"/></svg>Real Time Email Confirmation of Delivery</li>
    <li><svg viewBox="0 0 16 16"><path d="M2 2 L14 8 L2 14 L5 8 Z" fill="none" stroke="#1a5ba6" stroke-width="1.6" stroke-linejoin="round"/></svg>Photos of Material Placement</li>
    <li><svg viewBox="0 0 16 16"><path d="M2 2 L14 8 L2 14 L5 8 Z" fill="none" stroke="#1a5ba6" stroke-width="1.6" stroke-linejoin="round"/></svg>Before/After Photo of Driveway</li>
    <li><svg viewBox="0 0 16 16"><path d="M2 2 L14 8 L2 14 L5 8 Z" fill="none" stroke="#1a5ba6" stroke-width="1.6" stroke-linejoin="round"/></svg>Material List of Products Delivered</li>
    <li><svg viewBox="0 0 16 16"><path d="M2 2 L14 8 L2 14 L5 8 Z" fill="none" stroke="#1a5ba6" stroke-width="1.6" stroke-linejoin="round"/></svg>Homeowner Sign Off</li>
  </ul>

  <div class="worker-photo" role="img" aria-label="Photo of a smiling driver in a hi-vis vest holding the truck's tablet"></div>

  <p class="speech">Ever wonder if your material has been delivered?<br>We've got a solution for that!</p>

  <p class="call-label">Call now:</p>
  <p class="call-number">
    <svg viewBox="0 0 24 24"><path d="M6.6 10.8a15 15 0 0 0 6.6 6.6l2.2-2.2a1 1 0 0 1 1-.25 11.4 11.4 0 0 0 3.6.6 1 1 0 0 1 1 1V20a1 1 0 0 1-1 1A17 17 0 0 1 3 4a1 1 0 0 1 1-1h3.5a1 1 0 0 1 1 1 11.4 11.4 0 0 0 .6 3.6 1 1 0 0 1-.25 1z" fill="#1b2747"/></svg>
    +1 555 010 2468
  </p>

  <div class="web-band">
    <svg viewBox="0 0 20 20"><g fill="none" stroke="#fff" stroke-width="1.5"><circle cx="10" cy="10" r="8"/><ellipse cx="10" cy="10" rx="3.5" ry="8"/><path d="M2 10h16M3.5 6h13M3.5 14h13"/></g></svg>
    www.harborfinchbuild.com
  </div>
</main>
</body>
</html>
```